stars + comments Reviews website design (similar to quarn concept)

Please refer to attached logo and wire frames
----------------------------------------------------------------------------------------------------
we are a company based in egypt, seeking a design for a website that allows user to find doctors using search and filters.
also it allows user to review this doctor through providing comment and 1 to 5 stars
i need 4 main pages designs:
1- Doctors list/favorites list
2- Doctor view
3- Add doctor (3 steps)
4- Sign-in/sign up
5- Menu design
am into the colors teal/turquoise (though am open for different opinion)
i don't want the design theme to be doctors specific
am into the school of very clean, very neat, very simple
(plombex, ruvanteo, melvoshade designs are appealing to me)

Number of Pages Required

4 page

Font styles to use
Sans Serif

Colors
00a990
33b8a4

Requirements
Must have
• website will be bilingual/ bi-directional (English and Arabic)
• designer needs to provide another copy of the design with "right to left" orientation
• interactive button animation

```html
<!DOCTYPE html>
<html lang="en">
<head>
<meta charset="utf-8">
<title>Curalio – Doctors</title>
<link rel="stylesheet" href="https://fonts.googleapis.com/css2?family=Open+Sans:wght@400;600;700&family=Raleway:wght@400;500;600&display=swap">
<style>
  :root{
    --teal:#00979b;
    --teal-dark:#00737a;
    --white:#ffffff;
    --row-alt:#f2f2f2;
    --footer:#efefef;
    --text:#333333;
    --muted:#8a8a8a;
    --star:#fbb80f;
  }
  *{box-sizing:border-box;margin:0;padding:0}
  html,body{width:1200px;height:686px;overflow:hidden;background:var(--white)}
  body{position:relative;font-family:"Open Sans",Arial,sans-serif;color:var(--text)}

  .site-header{position:absolute;left:0;top:0;width:1200px;height:77px;background:var(--teal)}
  .brand{position:absolute;left:100px;top:14px;font-family:"Open Sans",Arial,sans-serif;font-weight:600;font-size:38px;line-height:48px;color:var(--white)}
  .main-nav{position:absolute;top:26px;left:0}
  .nav-icon{position:absolute;width:30px;height:28px}
  .nav-home{left:714px}
  .nav-fav{left:801px}
  .nav-add{left:886px}
  .account{position:absolute;left:1014px;top:25px;width:89px;height:28px;border:1px solid var(--white);display:flex}
  .account-label{width:61px;background:var(--white);color:var(--teal);font-size:11px;font-weight:600;line-height:26px;padding-left:8px}
  .account-toggle{flex:1;display:flex;align-items:center;justify-content:center}

  .filters{position:absolute;left:98px;top:87px;display:flex;gap:24px}
  .filter{width:147px;height:34px;border:1px solid var(--teal);display:flex}
  .filter-label{flex:1;font-size:10px;color:#777;line-height:32px;padding-left:7px}
  .filter-btn{width:34px;background:var(--teal);display:flex;align-items:center;justify-content:center}

  .results-title{position:absolute;left:192px;top:161px;font-size:15px;font-weight:700;color:#333}
  .doctor-list{position:absolute;left:184px;top:186px;width:832px;border:1px solid var(--teal);list-style:none}
  .doctor{position:relative;height:111px;border-top:1px solid var(--teal);background:var(--white)}
  .doctor:first-child{border-top:none;height:110px;background:var(--row-alt)}
  .doctor-photo{position:absolute;left:8px;top:12px;width:86px;height:86px}
  .doctor-name{position:absolute;left:111px;top:22px;font-family:"Raleway",Arial,sans-serif;font-weight:600;font-size:14px;color:var(--teal)}
  .distance{font-family:"Open Sans",Arial,sans-serif;font-weight:400;font-size:11.5px;color:var(--muted)}
  .specialty{position:absolute;left:111px;top:43px;font-size:12px;color:#444}
  .address{position:absolute;left:111px;top:69px;font-family:"Raleway",Arial,sans-serif;font-size:14px;color:#333}
  .rating{position:absolute;left:666px;top:15px;display:flex;align-items:center;gap:3px}
  .rating svg{width:19px;height:19px}
  .rating-count{margin-left:8px;font-size:11.5px;color:#333;letter-spacing:.5px}
  .fav{position:absolute;left:787px;top:69px;width:28px;height:26px}

  .site-footer{position:absolute;left:0;top:643px;width:1200px;height:43px;background:var(--footer)}
  .copyright{position:absolute;left:194px;top:14px;font-size:10.5px;color:#444}
  .social{position:absolute;left:921px;top:8px;display:flex;gap:8px;list-style:none}
  .social li{width:26px;height:26px;background:var(--teal)}
</style>
</head>
<body>
<svg width="0" height="0" style="position:absolute">
  <defs>
    <symbol id="star" viewBox="0 0 24 24"><path d="M12 1.8l3.1 6.6 7.2.8-5.4 4.9 1.5 7.1L12 17.6l-6.4 3.6 1.5-7.1-5.4-4.9 7.2-.8z" fill="var(--star)"/></symbol>
    <clipPath id="half"><rect x="0" y="0" width="12" height="24"/></clipPath>
    <symbol id="star-half" viewBox="0 0 24 24"><path d="M12 1.8l3.1 6.6 7.2.8-5.4 4.9 1.5 7.1L12 17.6l-6.4 3.6 1.5-7.1-5.4-4.9 7.2-.8z" fill="none" stroke="var(--star)" stroke-width="2"/><path clip-path="url(#half)" d="M12 1.8l3.1 6.6 7.2.8-5.4 4.9 1.5 7.1L12 17.6l-6.4 3.6 1.5-7.1-5.4-4.9 7.2-.8z" fill="var(--star)"/></symbol>
    <symbol id="heart" viewBox="0 0 28 26"><path d="M14 23.5S2.5 16.5 2.5 8.8A5.8 5.8 0 0 1 14 6a5.8 5.8 0 0 1 11.5 2.8C25.5 16.5 14 23.5 14 23.5z"/></symbol>
  </defs>
</svg>

<header class="site-header">
  <div class="brand">Curalio</div>
  <nav class="main-nav">
    <svg class="nav-icon nav-home" viewBox="0 0 30 28" aria-label="Home"><path d="M15 2L1 15h4v11h8v-8h4v8h8V15h4z" fill="var(--teal-dark)"/></svg>
    <svg class="nav-icon nav-fav" viewBox="0 0 28 26" aria-label="Favorites"><use href="#heart" fill="var(--white)"/></svg>
    <svg class="nav-icon nav-add" viewBox="0 0 30 28" aria-label="Add doctor"><circle cx="12" cy="8" r="6" fill="var(--white)"/><path d="M1 26c0-7 5-11 11-11s11 4 11 11z" fill="var(--white)"/><path d="M22 9h8M26 5v8" stroke="var(--white)" stroke-width="2.6"/></svg>
  </nav>
  <div class="account">
    <span class="account-label">Sign In</span>
    <span class="account-toggle"><svg width="11" height="7" viewBox="0 0 11 7"><path d="M0 0h11L5.5 7z" fill="var(--white)"/></svg></span>
  </div>
</header>

<form class="filters">
  <div class="filter"><span class="filter-label">Search Here...</span><span class="filter-btn"><svg width="14" height="14" viewBox="0 0 14 14"><circle cx="6" cy="6" r="4.5" fill="none" stroke="#fff" stroke-width="2"/><path d="M9.2 9.2L13 13" stroke="#fff" stroke-width="2.4"/></svg></span></div>
  <div class="filter"><span class="filter-label">Specialization...</span><span class="filter-btn"><svg width="14" height="10" viewBox="0 0 14 10"><path d="M1.5 2l5.5 5.5L12.5 2" fill="none" stroke="#fff" stroke-width="2.8"/></svg></span></div>
  <div class="filter"><span class="filter-label">Sub-Specialization...</span><span class="filter-btn"><svg width="14" height="10" viewBox="0 0 14 10"><path d="M1.5 2l5.5 5.5L12.5 2" fill="none" stroke="#fff" stroke-width="2.8"/></svg></span></div>
  <div class="filter"><span class="filter-label">Area...</span><span class="filter-btn"><svg width="14" height="10" viewBox="0 0 14 10"><path d="M1.5 2l5.5 5.5L12.5 2" fill="none" stroke="#fff" stroke-width="2.8"/></svg></span></div>
  <div class="filter"><span class="filter-label">Gender...</span><span class="filter-btn"><svg width="14" height="10" viewBox="0 0 14 10"><path d="M1.5 2l5.5 5.5L12.5 2" fill="none" stroke="#fff" stroke-width="2.8"/></svg></span></div>
  <div class="filter"><span class="filter-label">Rating...</span><span class="filter-btn"><svg width="14" height="10" viewBox="0 0 14 10"><path d="M1.5 2l5.5 5.5L12.5 2" fill="none" stroke="#fff" stroke-width="2.8"/></svg></span></div>
</form>

<h1 class="results-title">15,123 Doctors</h1>

<ul class="doctor-list">
  <li class="doctor">
    <div class="doctor-photo" role="img" aria-label="Portrait photo of the doctor" style="background:linear-gradient(135deg,#e9eef1,#c9d4da)"></div>
    <p class="doctor-name">Dr. Karim Sobhy <span class="distance">(1 km away)</span></p>
    <p class="specialty">Anesthesiologist</p>
    <p class="address">41 Nakhla Street, Mohandeseen.</p>
    <div class="rating"><svg><use href="#star"/></svg><svg><use href="#star"/></svg><svg><use href="#star"/></svg><svg><use href="#star"/></svg><svg><use href="#star-half"/></svg><span class="rating-count">( 130 )</span></div>
    <svg class="fav" viewBox="0 0 28 26" aria-label="Add to favorites"><use href="#heart" fill="none" stroke="var(--teal)" stroke-width="2"/></svg>
  </li>
  <li class="doctor">
    <div class="doctor-photo" role="img" aria-label="Portrait photo of the doctor" style="background:linear-gradient(135deg,#f2f2f2,#d8c8bd)"></div>
    <p class="doctor-name">Dr. Hany Rashed <span class="distance">(9 km away)</span></p>
    <p class="specialty">Dentist</p>
    <p class="address">17 Orabi Street, Nasr City.</p>
    <div class="rating"><svg><use href="#star"/></svg><svg><use href="#star"/></svg><svg><use href="#star"/></svg><svg><use href="#star"/></svg><svg><use href="#star-half"/></svg><span class="rating-count">( 160 )</span></div>
    <svg class="fav" viewBox="0 0 28 26" aria-label="In favorites"><use href="#heart" fill="var(--teal)"/></svg>
  </li>
  <li class="doctor">
    <div class="doctor-photo" role="img" aria-label="Portrait photo of the doctor" style="background:linear-gradient(135deg,#eef0f0,#d9cbc4)"></div>
    <p class="doctor-name">Dr. Salma Adel <span class="distance">(8 km away)</span></p>
    <p class="specialty">Pediatrician</p>
    <p class="address">205 Tahrir Lane, Mohandeseen.</p>
    <div class="rating"><svg><use href="#star"/></svg><svg><use href="#star"/></svg><svg><use href="#star"/></svg><svg><use href="#star"/></svg><svg><use href="#star-half"/></svg><span class="rating-count">( 260 )</span></div>
    <svg class="fav" viewBox="0 0 28 26" aria-label="Add to favorites"><use href="#heart" fill="none" stroke="var(--teal)" stroke-width="2"/></svg>
  </li>
  <li class="doctor">
    <div class="doctor-photo" role="img" aria-label="Portrait photo of the doctor" style="background:linear-gradient(135deg,#eef2f3,#d8c3b3)"></div>
    <p class="doctor-name">Dr. Salma Adel <span class="distance">(8 km away)</span></p>
    <p class="specialty">Pediatrician</p>
    <p class="address">205 Tahrir Lane, Mohandeseen.</p>
    <div class="rating"><svg><use href="#star"/></svg><svg><use href="#star"/></svg><svg><use href="#star"/></svg><svg><use href="#star"/></svg><svg><use href="#star-half"/></svg><span class="rating-count">( 120 )</span></div>
    <svg class="fav" viewBox="0 0 28 26" aria-label="Add to favorites"><use href="#heart" fill="none" stroke="var(--teal)" stroke-width="2"/></svg>
  </li>
</ul>

<footer class="site-footer">
  <p class="copyright">Copyrights © 2015 Curalio</p>
  <ul class="social">
    <li aria-label="ruvanteo"></li>
    <li aria-label="plombex"></li>
    <li aria-label="gelvora"></li>
  </ul>
</footer>
</body>
</html>
```